Book cover for book about Climate Change

Looking for a clean, bold, and attractive cover for a mass-market paperback (5.5"x 8.5") about solving the climate change problem. Title is either "When Rivers Learn to Sing” or A Lantern Over Quiet Fields” (your choice), subtitle is "A five-step plan to reverse climate change — to ensure that your grandchildren will live on a clean and comfortable planet," author is Dale Pruitt. Thinking that it *might* feature an image of Earth (or a portion thereof) and its very thin layer of atmosphere -- but STRONGLY encourage other ideas too!

Requirements
Nice to have
• Keep it positive — NOT scary doom-and-gloom

```html
<!DOCTYPE html>
<html lang="en">
<head>
<meta charset="utf-8">
<title>A Lantern Over Quiet Fields — Dale Pruitt</title>
<link rel="stylesheet" href="https://fonts.googleapis.com/css2?family=Bebas+Neue&family=Poppins:wght@600;700&display=swap">
<style>
  :root {
    --backdrop: #c4c4c4;
    --cover-grey: #e4e4e4;
    --cover-glow: #ffffff;
    --ink-black: #1c1c1c;
    --ink-blue: #0d5aa7;
    --ruler-blue: #2f66a8;
    --planet-deep: #1e2a4f;
    --planet-mid: #4a5f8a;
    --planet-light: #e9ecef;
  }
  * { margin: 0; padding: 0; box-sizing: border-box; }
  html, body {
    width: 1200px;
    height: 1200px;
    overflow: hidden;
    background: var(--backdrop);
  }
  .book-cover {
    position: absolute;
    left: 182px;
    top: 29px;
    width: 835px;
    height: 1142px;
    background:
      radial-gradient(circle at 50% 56%, var(--cover-glow) 0, rgba(255,255,255,0.6) 180px, rgba(255,255,255,0) 330px),
      var(--cover-grey);
    overflow: hidden;
  }
  .cover-art {
    position: absolute;
    left: 0;
    top: 0;
  }
  .display-type {
    font-family: "Bebas Neue", "Oswald", "Arial Narrow", sans-serif;
    font-weight: 400;
  }
  .title-top { fill: var(--ink-black); }
  .title-bottom, .author-name { fill: var(--ink-blue); }
  .scale-number {
    font-family: "Poppins", Arial, sans-serif;
    font-weight: 600;
    font-size: 38px;
    fill: var(--ink-blue);
  }
  .subtitle {
    position: absolute;
    top: 849px;
    left: 0;
    width: 100%;
    text-align: center;
    font-family: "Poppins", Arial, sans-serif;
    font-weight: 700;
    font-size: 24px;
    line-height: 36px;
    color: var(--ink-black);
    text-transform: uppercase;
    letter-spacing: -0.4px;
    white-space: nowrap;
  }
  .subtitle-accent { color: var(--ruler-blue); }
</style>
</head>
<body>
  <main class="book-cover">
    <svg class="cover-art" width="835" height="1142" viewBox="0 0 835 1142" xmlns="http://www.w3.org/2000/svg">
      <defs>
        <radialGradient id="planet-fill" cx="45%" cy="40%" r="65%">
          <stop offset="0" stop-color="var(--planet-light)"/>
          <stop offset="0.45" stop-color="var(--planet-mid)"/>
          <stop offset="1" stop-color="var(--planet-deep)"/>
        </radialGradient>
      </defs>

      <g class="book-title" role="heading" aria-level="1">
        <text class="display-type title-top" x="86" y="206" font-size="168" textLength="669" lengthAdjust="spacingAndGlyphs">A LANTERN OVER</text>
        <text class="display-type title-bottom" x="86" y="346" font-size="168" textLength="669" lengthAdjust="spacingAndGlyphs">QUIET FIELDS</text>
      </g>

      <g class="scale-ticks" stroke="var(--ruler-blue)" stroke-width="3.5">
        <line x1="18" y1="568" x2="18" y2="643"/>
        <line x1="41" y1="568" x2="41" y2="643"/>
        <line x1="65" y1="547" x2="65" y2="643"/>
        <line x1="87" y1="568" x2="87" y2="643"/>
        <line x1="110" y1="568" x2="110" y2="643"/>
        <line x1="132" y1="568" x2="132" y2="643"/>
        <line x1="155" y1="547" x2="155" y2="643"/>
        <line x1="178" y1="568" x2="178" y2="643"/>
        <line x1="200" y1="568" x2="200" y2="643"/>
        <line x1="222" y1="568" x2="222" y2="643"/>
        <line x1="245" y1="547" x2="245" y2="643"/>
        <line x1="610" y1="568" x2="610" y2="643"/>
        <line x1="637" y1="547" x2="637" y2="643"/>
        <line x1="660" y1="568" x2="660" y2="643"/>
        <line x1="682" y1="568" x2="682" y2="643"/>
        <line x1="705" y1="568" x2="705" y2="643"/>
        <line x1="727" y1="547" x2="727" y2="643"/>
        <line x1="750" y1="568" x2="750" y2="643"/>
        <line x1="773" y1="568" x2="773" y2="643"/>
        <line x1="796" y1="547" x2="796" y2="643"/>
      </g>
      <text class="scale-number" x="65" y="521" text-anchor="middle">1</text>
      <text class="scale-number" x="155" y="521" text-anchor="middle">2</text>
      <text class="scale-number" x="245" y="521" text-anchor="middle">3</text>
      <text class="scale-number" x="637" y="521" text-anchor="middle">4</text>
      <text class="scale-number" x="727" y="521" text-anchor="middle">5</text>
      <circle cx="426" cy="596" r="190" fill="url(#planet-fill)" role="img" aria-label="Photograph of planet Earth seen from space, showing Africa and swirling white clouds over blue oceans"/>

      <text class="display-type author-name" x="250" y="1115" font-size="126" textLength="336" lengthAdjust="spacingAndGlyphs">DALE PRUITT</text>
    </svg>

    <p class="subtitle">
      <span class="subtitle-accent">A five-step</span> plan to reverse climate<br>
      change to ensure that your grandchildren<br>
      will live on a clean and comfortable planet
    </p>
  </main>
</body>
</html>
```